StayCrewly.com homepage

We need a new homepage for our new domain.

StayCrewly.com

The colors to be used are the ones in our logo (attached) and in the current log in page host.lodgenestly.com

Its important its a ONE PAGE site where you can scroll and elements appear while scrolling down.

It has to be simple to the point similar to the chatterbook log in page.

The current log in box and registration box have to stay but can be moved around obviously.

Also the video as on our current page www.lodgenestly.com needs to have its place on the homepage.

Slogan

StayCrewly.com - The Rental Teamwork Hub.

Vacation rental managers and hosts can now team up with a booking team. Its easy to instantly improve your online booking management. Be on all the best booking sites without all the hassle. Improve your current strategy and save loads of time which you can spend on the satisfaction of your guests.

Something like that not too long.

I look forward to seeing your proposed designs.

In the attachment is our logo and a screenshot of our backend so the design will match nicely

Target Market(s)

Owners and property managers of vacation rentals world wide

Industry/Entity Type

Domain

Number of Pages Required

1 page

Requirements
Nice to have
• Smooth scrolling elements

```html
<!DOCTYPE html>
<html lang="en">
<head>
<meta charset="utf-8">
<title>StayCrewly.com – The Rental Teamwork Hub</title>
<link href="https://fonts.googleapis.com/css2?family=Open+Sans:wght@400;600;700&family=Ubuntu:wght@400;500;700&display=swap" rel="stylesheet">
<style>
:root{
  --blue:#0c3fa6;
  --blue-deep:#0a2d84;
  --blue-light:#1c5fcc;
  --orange:#f15a1c;
  --orange-light:#f7782f;
  --grey-bg:#efefef;
  --grey-line:#d6d6d6;
  --text:#333;
  --muted:#8a8a8a;
  --white:#fff;
}
*{margin:0;padding:0;box-sizing:border-box}
html,body{width:1200px;height:2579px;overflow:hidden}
body{position:relative;font-family:"Open Sans",Arial,sans-serif;color:var(--text);background:var(--white)}
.abs{position:absolute}
.heading{font-family:"Ubuntu","Open Sans",sans-serif}

/* header */
.site-header{left:0;top:0;width:1200px;height:115px;background:linear-gradient(#f6f6f6,#e4e4e4)}
.brand{left:56px;top:14px;display:flex;align-items:center;gap:10px}
.brand-mark{width:34px;height:34px;border-radius:50%;background:var(--orange)}
.brand-name{font-family:"Ubuntu",sans-serif;font-weight:700;font-size:30px;color:var(--blue)}
.top-contact{right:52px;top:8px;display:flex;align-items:center;gap:14px}
.round-icon{width:36px;height:36px;border-radius:50%;display:flex;align-items:center;justify-content:center}
.round-icon.orange{background:var(--orange)}
.round-icon.blue{background:var(--blue)}
.call{font-size:11px;line-height:1.1;color:var(--blue);font-weight:700}
.call span{display:block;font-size:15px;font-weight:400;color:#333}
.main-nav{left:567px;top:48px;display:flex;height:67px}
.main-nav a{display:flex;align-items:center;justify-content:center;font-size:12px;font-weight:600;color:#333;text-decoration:none;text-transform:uppercase;width:128px}
.main-nav a.active{background:var(--blue);color:var(--white);width:87px;margin-right:14px}

/* hero */
.hero{left:0;top:115px;width:1200px;height:664px;background:radial-gradient(ellipse at 60% 70%,#7b6a5c 0%,#4f4f55 40%,#2c3038 100%)}
.hero-title{left:0;top:248px;width:1200px;text-align:center;color:var(--white);font-size:28px;font-weight:500}
.hero-col{color:var(--white)}
.hero-col h2{font-family:"Ubuntu",sans-serif;font-weight:500;font-size:38px;margin-bottom:8px}
.hero-col p{font-size:16px;line-height:24px}
.hero-host{right:667px;top:318px;text-align:right}
.hero-guest{left:645px;top:324px}
.btn{display:inline-flex;align-items:center;justify-content:center;color:var(--white);font-size:13px;font-weight:600;text-transform:uppercase;text-decoration:none}
.btn-blue{background:var(--blue)}
.btn-orange{background:var(--orange)}
.hero-host .btn{width:186px;height:43px;margin-top:26px;margin-right:8px}
.hero-guest .btn{width:188px;height:44px;margin-top:26px}
.slider-arrow{width:38px;height:38px;border-radius:50%;background:#eee;top:339px;display:flex;align-items:center;justify-content:center}
.slider-dots{top:689px;left:540px;display:flex;gap:8px}
.slider-dots i{width:14px;height:14px;border-radius:50%;border:2px solid #ddd}
.slider-dots i.on{background:#ddd}

/* feature band */
.feature-band{left:0;top:779px;width:1200px;height:161px;background:linear-gradient(var(--blue-light),var(--blue-deep))}
.feature{width:220px;top:738px;text-align:center;color:var(--white);font-size:12px;line-height:17px}
.feature .badge{width:84px;height:84px;margin:0 auto 18px;border-radius:50%;background:var(--orange);border:4px solid var(--white);display:flex;align-items:center;justify-content:center}
.band-arrow{top:845px;color:#9cb5e8;font-size:12px}

/* intro */
.intro-title{left:0;top:974px;width:1200px;text-align:center;font-size:27px;color:var(--blue-deep)}
.intro-title em{font-style:normal;color:var(--orange)}
.intro-box{left:107px;top:1040px;width:994px;height:407px;border:1px solid var(--grey-line)}
.intro-text{left:140px;top:1076px;width:420px;text-align:center}
.intro-text h3{font-size:15px;font-weight:600;color:#222;margin-bottom:22px}
.intro-text p{font-size:12px;line-height:28px;color:var(--muted);margin-bottom:18px}
.intro-text .btn{width:134px;height:49px;margin-top:4px}
.intro-divider{left:590px;top:1070px;width:1px;height:350px;background:var(--grey-line)}
.video-title{left:600px;top:1085px;width:500px;text-align:center;font-size:15px;color:#222}
.video{left:631px;top:1133px;width:440px;height:287px;background:linear-gradient(#555,#3a3a3a);display:flex;align-items:center;justify-content:center}
.play{width:70px;height:70px;border-radius:50%;background:rgba(255,255,255,.9);display:flex;align-items:center;justify-content:center}

/* partners */
.partners{left:0;top:1480px;width:1200px;height:205px;background:var(--grey-bg)}
.partner{top:1509px;width:206px;height:109px;background:var(--white);border:1px solid var(--grey-line);display:flex;align-items:center;justify-content:center;font-size:21px;font-weight:600;color:#555}
.partner-dots{top:1647px;left:571px;display:flex;gap:10px}
.partner-dots i{width:13px;height:13px;border-radius:50%;background:#555}
.partner-dots i.on{background:var(--orange)}

/* city */
.city{left:0;top:1708px;width:1200px;height:314px;background:linear-gradient(var(--blue),var(--blue-deep))}
.city-item{top:1752px;width:150px;text-align:center;color:var(--white);font-size:17px}
.city-item svg{display:block;margin:0 auto 14px;height:100px}
.city-cta{left:206px;top:1918px;width:787px;height:69px;background:var(--orange);color:var(--white);font-size:22px;display:flex;align-items:center;justify-content:center}

/* cards */
.card-image{top:2056px;height:256px}
.card-image.tools{left:48px;width:516px;background:linear-gradient(135deg,#e0358c 0%,#f3e86a 55%,#3fc6c2 100%)}
.card-image.mobile{left:636px;width:516px;background:linear-gradient(135deg,#e0358c 0%,#f3e86a 55%,#3fc6c2 100%)}
.card-frame{top:2222px;height:222px;border:2px solid #ccc;border-top:none;background:var(--white)}
.card-body{top:2229px;height:208px;color:var(--white);text-align:center;padding:20px 20px}
.card-body.blue{left:103px;width:406px;background:var(--blue)}
.card-body.orange{left:693px;width:409px;background:var(--orange)}
.card-body h4{font-weight:400;font-size:17px;line-height:28px;margin-bottom:10px}
.card-body p{font-size:11.5px;line-height:17px}
.card-body.blue p{text-align:justify}
.store-badges{display:flex;gap:22px;justify-content:center;margin-top:20px}
.store-badges i{width:152px;height:54px;background:#111;border:2px solid #ddd;border-radius:8px}
.card-toggle{top:2399px;width:56px;height:56px;border-radius:50%;border:4px solid var(--white);display:flex;align-items:center;justify-content:center}

/* footer */
.site-footer{left:0;top:2503px;width:1200px;height:76px;background:var(--blue-deep);color:var(--white);font-size:11px}
.site-footer p{position:absolute;left:54px;top:31px}
.social{position:absolute;left:1003px;top:23px;display:flex;gap:10px}
.social i{width:27px;height:27px;border:1px solid var(--white)}
</style>
</head>
<body>

<header class="abs site-header">
  <div class="abs brand"><span class="brand-mark"></span><span class="brand-name">StayCrewly.com</span></div>
  <div class="abs top-contact">
    <span class="round-icon orange"><svg width="16" height="16" viewBox="0 0 16 16"><rect x="3" y="7" width="10" height="8" fill="#fff"/><path d="M5 7V5a3 3 0 0 1 6 0" stroke="#fff" stroke-width="2" fill="none"/></svg></span>
    <span class="round-icon blue"><svg width="16" height="16" viewBox="0 0 16 16"><path d="M3 2l3 0 1 4-2 1a8 8 0 0 0 4 4l1-2 4 1 0 3c-7 1-12-4-11-11z" fill="#fff"/></svg></span>
    <div class="call">CALL NOW<span>123-456-7890</span></div>
  </div>
  <nav class="abs main-nav">
    <a class="active" href="#">Home</a><a href="#">For Who?</a><a href="#">Team Up</a><a href="#">The Tools</a><a href="#" style="width:110px">Pricing</a>
  </nav>
</header>

<section class="abs hero" role="img" aria-label="Photo of hands typing on a laptop keyboard with network graphics overlay"></section>
<h1 class="abs hero-title heading">The Booking Collaboration Platform</h1>
<div class="abs hero-col hero-host">
  <h2>Hosting Community</h2>
  <p>Improve your guest experience<br>Booking team collaboration platform<br>Connect with local hosts and property managers</p>
  <a class="btn btn-blue" href="#">Host Signup / Login</a>
</div>
<div class="abs hero-col hero-guest">
  <h2>Guest Community</h2>
  <p>Speedy Guest attention<br>Best price guaranteed direct bookings<br>Great services, discounts, add-ons and Travel insurance</p>
  <a class="btn btn-orange" href="#">Guest Signup / Login</a>
</div>
<span class="abs slider-arrow" style="left:46px"><svg width="12" height="14"><path d="M9 2L3 7l6 5" stroke="#333" stroke-width="2.5" fill="none"/></svg></span>
<span class="abs slider-arrow" style="left:1112px"><svg width="12" height="14"><path d="M3 2l6 5-6 5" stroke="#333" stroke-width="2.5" fill="none"/></svg></span>
<div class="abs slider-dots"><i></i><i></i><i class="on"></i><i></i><i></i></div>

<section class="abs feature-band"></section>
<span class="abs band-arrow" style="left:22px">◀</span>
<span class="abs band-arrow" style="left:1160px">▶</span>
<div class="abs feature" style="left:34px"><div class="badge"><svg width="34" height="34" viewBox="0 0 24 24"><path d="M12 2l3 7 7 .6-5.3 4.6 1.6 7L12 17.5 5.7 21.2l1.6-7L2 9.6 9 9z" fill="#fff"/></svg></div>Improve the guest experience<br>for more 5 star reviews</div>
<div class="abs feature" style="left:263px"><div class="badge"><svg width="34" height="34" viewBox="0 0 24 24" fill="none" stroke="#fff" stroke-width="2"><rect x="3" y="5" width="15" height="15" rx="2"/><path d="M10 14l9-9 2 2-9 9h-2z" fill="#fff"/></svg></div>Process modifications<br>and upload your properties<br>to more booking sites</div>
<div class="abs feature" style="left:485px"><div class="badge"><svg width="34" height="34" viewBox="0 0 24 24" fill="none" stroke="#fff" stroke-width="2.2"><circle cx="12" cy="12" r="9"/><path d="M12 7v5h4"/></svg></div>A service oriented contact for<br>your guests whenever<br>needed</div>
<div class="abs feature" style="left:712px"><div class="badge"><svg width="34" height="34" viewBox="0 0 24 24" fill="none" stroke="#fff" stroke-width="2"><rect x="3" y="5" width="18" height="16" rx="1"/><path d="M3 10h18M8 3v4M16 3v4M7 14h2M11 14h2M15 14h2M7 17h2M11 17h2"/></svg></div>Increase occupancy<br>rate and boost overall<br>success</div>
<div class="abs feature" style="left:935px"><div class="badge"><svg width="34" height="34" viewBox="0 0 24 24" fill="none" stroke="#fff" stroke-width="2.4"><path d="M20 4l-7 7M13 6v5h5M4 20l7-7M6 13h5v5"/></svg></div>Actively monitor rates<br>and apply last minutes, increas-<br>es or decreases</div>

<h2 class="abs intro-title heading">THe First Social <em>Booking Network</em></h2>
<div class="abs intro-box"></div>
<div class="abs intro-text">
  <h3>LodgeNestly is a New Social Booking Network</h3>
  <p>Vacation Rental Hosts, Property Managers and Service Providers can now find each other, connect and chat amongst themselves for sharing reservation opportunities, services or anything imaginable in a convenient social environment.</p>
  <p>The Social Booking Network is absolutely FREE. However if you want to save time and get really professional about increasing your bookings you could also have your very own Booking Team.</p>
  <a class="btn btn-blue" href="#">Read More ▸</a>
</div>
<div class="abs intro-divider"></div>
<h3 class="abs video-title">LodgeNestly. Social Booking Network &amp; Bunkly Assistant</h3>
<div class="abs video" role="img" aria-label="Intro video: getting started is easy on www.lodgenestly.com"><span class="play"><svg width="26" height="28"><path d="M4 2l20 12-20 12z" fill="#333"/></svg></span></div>

<section class="abs partners"></section>
<div class="abs partner" style="left:48px">HavenRoam</div>
<div class="abs partner" style="left:270px">bunkly</div>
<div class="abs partner" style="left:494px">Roomvia.com</div>
<div class="abs partner" style="left:716px">TripLatch</div>
<div class="abs partner" style="left:940px">Wandoro</div>
<div class="abs partner-dots"><i></i><i class="on"></i><i></i></div>

<section class="abs city"></section>
<div class="abs city-item" style="left:62px"><svg viewBox="0 0 80 100" width="80"><path d="M6 14h68L40 54z" fill="none" stroke="#fff" stroke-width="4"/><path d="M40 54v36M22 92h36" stroke="#fff" stroke-width="4"/><circle cx="62" cy="8" r="5" fill="none" stroke="#fff" stroke-width="3"/><path d="M58 12l-16 20" stroke="#fff" stroke-width="3"/></svg>Night Life</div>
<div class="abs city-item" style="left:245px"><svg viewBox="0 0 100 100" width="100"><g fill="none" stroke="#fff" stroke-width="3"><path d="M30 40a20 20 0 0 1 40 0zM10 92V30M90 92V30M28 92V50h44v42M4 92h92M40 92V74h20v18"/><path d="M50 12v8M10 30l-4-14M90 30l4-14"/></g></svg>Events &amp; Tickets</div>
<div class="abs city-item" style="left:432px"><svg viewBox="0 0 110 100" width="110"><path d="M10 80a45 45 0 0 1 90 0z" fill="#fff"/><rect x="4" y="84" width="102" height="8" fill="#fff"/><circle cx="55" cy="30" r="6" fill="#fff"/></svg>Local Cuisine</div>
<div class="abs city-item" style="left:619px"><svg viewBox="0 0 110 100" width="110"><g fill="#fff"><path d="M10 95V45h25v50zM38 95V5l35 15v75zM76 95V50h28v45z"/></g><g fill="#1546ad"><rect x="16" y="55" width="6" height="6"/><rect x="25" y="55" width="6" height="6"/><rect x="16" y="70" width="6" height="6"/><rect x="25" y="70" width="6" height="6"/><rect x="46" y="25" width="7" height="7"/><rect x="58" y="30" width="7" height="7"/><rect x="46" y="45" width="7" height="7"/><rect x="58" y="48" width="7" height="7"/><rect x="46" y="65" width="7" height="7"/><rect x="58" y="66" width="7" height="7"/><rect x="82" y="60" width="6" height="6"/><rect x="92" y="60" width="6" height="6"/><rect x="82" y="75" width="6" height="6"/><rect x="92" y="75" width="6" height="6"/></g></svg>Getting Around</div>
<div class="abs city-item" style="left:806px"><svg viewBox="0 0 100 100" width="100"><path d="M50 30c-2 25 0 45 8 66h-10c-6-20-8-40-4-66z" fill="#fff"/><path d="M48 30C35 12 15 14 6 30c14-8 28-6 42 0zM50 30c10-18 30-22 44-10-16-2-30 2-44 10zM48 32C30 30 18 40 14 56c10-14 22-20 34-24zM52 32c18 0 30 10 32 26-8-14-20-20-32-26z" fill="#fff"/></svg>Best Spots</div>
<div class="abs city-item" style="left:993px"><svg viewBox="0 0 110 100" width="110"><g fill="none" stroke="#fff" stroke-width="4"><path d="M5 35l20-25h60l20 25-50 55z"/><path d="M5 35h100M35 35l20 55 20-55M25 10l10 25 20-25 20 25 10-25"/></g></svg>Souvenirs</div>
<div class="abs city-cta">Share your City with the Guest Experience Manager</div>

<div class="abs card-image tools" role="img" aria-label="Laptop showing the booking calendar and rate management dashboard"></div>
<div class="abs card-frame" style="left:90px;width:432px"></div>
<div class="abs card-body blue">
  <h4>Stay ahead with the best VR tools known<br>to CrewKind</h4>
  <p>The most advanced booking tools allow you and your booking team to focus on whats really important. Optimizing your listings and reviews, providing the best possible guest experience and yielding up or down the nightly rates based on market developments and constant demand fluctuations.</p>
</div>
<span class="abs card-toggle" style="left:278px;background:var(--orange)"><svg width="16" height="12"><path d="M2 3l6 6 6-6" stroke="#fff" stroke-width="3" fill="none"/></svg></span>

<div class="abs card-image mobile" role="img" aria-label="Hand holding a smartphone showing the mobile app"></div>
<div class="abs card-frame" style="left:682px;width:428px"></div>
<div class="abs card-body orange">
  <h4>Connect to your Network From Anywhere</h4>
  <p>Available on Droidia and coming soon to the<br>Pomme app store</p>
  <div class="store-badges"><i></i><i></i></div>
</div>
<span class="abs card-toggle" style="left:864px;background:var(--blue)"><svg width="16" height="12"><path d="M2 3l6 6 6-6" stroke="#fff" stroke-width="3" fill="none"/></svg></span>

<footer class="abs site-footer">
  <p>Copyright 2016 Company Name. All Rights Reserved.</p>
  <div class="social"><i></i><i></i><i></i><i></i></div>
</footer>

</body>
</html>
```